Create a professional, eye-catching business card design that reflects the values and services of Brookfern Veterinary Hospital. we provide veterinary services and the business card should be a memorable representation of the clinic and align with its branding and mission. our tag line is "Gentle Hands, Caring Hearts for Every Pet"
Use clean, modern typography. Prioritize readability and professionalism. We would like to see designs that use the color blue, as in the logo example. the final design should communicate professionalism and care, with attention to detail.

```html
<!DOCTYPE html>
<html lang="en">
<head>
<meta charset="utf-8">
<title>Brookfern Veterinary Hospital – Business Card</title>
<link href="https://fonts.googleapis.com/css2?family=Montserrat:ital,wght@0,400;0,500;0,700;0,800;1,700&display=swap" rel="stylesheet">
<style>
  :root {
    --navy: #22386a;
    --white: #ffffff;
    --tagline: #f3d31a;
    --ink: #22386a;
    --ink-soft: #3a4d78;
    --backdrop-light: #e6e8ec;
    --backdrop-dark: #aeb4be;
  }
  * { margin: 0; padding: 0; box-sizing: border-box; }
  html, body { width: 1200px; height: 675px; overflow: hidden; }
  body {
    background: linear-gradient(160deg, var(--backdrop-light) 0%, #d3d7dd 55%, var(--backdrop-dark) 100%);
    font-family: "Montserrat", Arial, sans-serif;
    position: relative;
  }
  .card {
    position: absolute;
    top: 194px;
    width: 500px; height: 286px;
    border-radius: 4px;
    box-shadow: 0 14px 30px rgba(30, 40, 60, 0.28), 0 2px 6px rgba(30, 40, 60, 0.18);
    overflow: hidden;
  }
  /* Front */
  .card--front {
    left: 70px;
    background: var(--navy);
    color: var(--white);
    display: flex; flex-direction: column; align-items: center; justify-content: center;
  }
  .brand { display: flex; flex-direction: column; align-items: center; }
  .brand__circle {
    width: 58px; height: 58px; border-radius: 50%;
    border: 2px solid currentColor;
    margin-bottom: 14px;
  }
  .brand__name {
    font-weight: 800;
    text-transform: uppercase;
    text-align: center;
    line-height: 1.15;
    letter-spacing: 0.04em;
    font-size: 22px;
    white-space: nowrap;
  }
  .card--front .brand__name { color: var(--white); }
  .tagline {
    margin-top: 22px;
    color: var(--tagline);
    font-style: italic;
    font-weight: 700;
    font-size: 15px;
    letter-spacing: 0.03em;
  }
  /* Back */
  .card--back {
    left: 630px;
    background: var(--white);
    color: var(--ink);
    border-bottom: 4px solid var(--navy);
  }
  .contact { position: absolute; left: 34px; top: 66px; }
  .contact__name { font-weight: 700; font-size: 20px; color: var(--ink); letter-spacing: 0.01em; }
  .contact__role { font-weight: 500; font-size: 11.5px; color: var(--ink-soft); margin-top: 2px; letter-spacing: 0.06em; }
  .contact__address {
    font-style: normal; font-size: 11.5px; color: var(--ink-soft);
    margin-top: 10px; line-height: 1.55; letter-spacing: 0.04em;
  }
  .contact__list { list-style: none; margin-top: 12px; }
  .contact__item {
    display: flex; align-items: center; gap: 9px;
    font-size: 11.5px; color: var(--ink-soft);
    line-height: 1; margin-bottom: 9px; letter-spacing: 0.04em;
  }
  .contact__icon { width: 13px; height: 13px; flex: none; fill: var(--ink); }
  .contact__icon--line { fill: none; stroke: var(--ink); stroke-width: 2; }
  .card--back .brand { position: absolute; right: 20px; top: 66px; width: 210px; }
  .card--back .brand__circle { width: 52px; height: 52px; }
  .card--back .brand__name { color: var(--ink); font-size: 14px; }
</style>
</head>
<body>
  <section class="card card--front" aria-label="Business card front">
    <div class="brand">
      <span class="brand__circle" aria-hidden="true"></span>
      <p class="brand__name">Brookfern<br>Veterinary Hospital</p>
    </div>
    <p class="tagline">Gentle Hands, Caring Hearts for Every Pet</p>
  </section>

  <section class="card card--back" aria-label="Business card back">
    <div class="contact">
      <h1 class="contact__name">Daniel Ashcombe</h1>
      <p class="contact__role">Owner</p>
      <address class="contact__address">12 Wattle Grove Road,<br>Greenmount, WA 6056</address>
      <ul class="contact__list">
        <li class="contact__item">
          <svg class="contact__icon" viewBox="0 0 24 24" aria-hidden="true"><path d="M6.6 10.8a15.1 15.1 0 0 0 6.6 6.6l2.2-2.2c.3-.3.7-.4 1-.2 1.1.4 2.3.6 3.6.6.6 0 1 .4 1 1V20c0 .6-.4 1-1 1A17 17 0 0 1 3 4c0-.6.4-1 1-1h3.5c.6 0 1 .4 1 1 0 1.3.2 2.5.6 3.6.1.3 0 .7-.2 1z"/></svg>
          (08) 9410 2834
        </li>
        <li class="contact__item">
          <svg class="contact__icon" viewBox="0 0 24 24" aria-hidden="true"><path d="M2 5h20v14H2z M4 7v.4l8 5.2 8-5.2V7z" fill-rule="evenodd"/></svg>
          reception@brookfernvet.com.au
        </li>
        <li class="contact__item">
          <svg class="contact__icon contact__icon--line" viewBox="0 0 24 24" aria-hidden="true"><circle cx="12" cy="12" r="9"/><ellipse cx="12" cy="12" rx="4" ry="9"/><path d="M3 12h18M5 7h14M5 17h14"/></svg>
          www.brookfernvet.com.au
        </li>
      </ul>
    </div>
    <div class="brand">
      <span class="brand__circle" aria-hidden="true"></span>
      <p class="brand__name">Brookfern<br>Veterinary Hospital</p>
    </div>
  </section>
</body>
</html>
```